update of B2B website and conversion to single page

The current website needs to be modernized. I want what is commonly called a single page website. It is not actually a single page. See some examples here:
https://www.brivolane.example/
https://www.quenzo.example/
https://www.tarnwickhub.example/
Most or all graphics will be replaced.
Please see the attached spreadsheet for a rough draft of the home page layout. Convert the existing website at https://www.zorbilinfo.example/ to a single page website. We will provide the page content. You will provide all of the design, graphics, development, production deployment. etc. The look and feel should be corporate, polished, premium.

```html
<!DOCTYPE html>
<html lang="en">
<head>
<meta charset="utf-8">
<title>Zorbil Data – Enterprise Data Quality and Master Data Management</title>
<link rel="stylesheet" href="https://fonts.googleapis.com/css2?family=Open+Sans:wght@400;600;700&family=Montserrat:wght@500;600&display=swap">
<style>
:root{
  --navy:#0f1d4a;
  --charcoal:#1c1d22;
  --yellow:#f2b90f;
  --accent:#2b3aa8;
  --ink:#222630;
  --muted:#6b7080;
  --line:#d9dbe3;
  --cream:#fdf8e6;
  --grey-band:#c9cacd;
  --footer:#17181c;
  --footer-bar:#0e0f12;
  --footer-text:#cfd0d4;
  --send:#2f7be0;
  --white:#ffffff;
}
*{box-sizing:border-box;margin:0;padding:0}
html,body{width:1200px;height:3040px;overflow:hidden}
body{font-family:"Open Sans",Arial,sans-serif;color:var(--ink);background:var(--white);position:relative}
ul{list-style:none}

/* header */
.site-header{position:absolute;top:0;left:0;width:1200px;height:100px;background:var(--white);display:flex;align-items:center;justify-content:space-between;padding:0 90px 0 110px;box-shadow:0 2px 6px rgba(0,0,0,.06);z-index:3}
.brand-name{font-size:28px;font-weight:600;color:var(--ink);line-height:1}
.main-nav{display:flex;gap:34px;font-size:15px;font-weight:600;color:var(--ink)}
.main-nav .active{color:var(--accent)}

/* hero */
.hero{position:absolute;top:100px;left:0;width:1200px;height:780px}
.hero-photo{position:absolute;inset:0;background:radial-gradient(ellipse at 50% 55%,#4d6a96 0%,#243a62 35%,#101d36 70%,#070d1a 100%)}
.hero-text{position:absolute;top:190px;width:100%;text-align:center;color:var(--white)}
.hero-title{font-size:68px;font-weight:600;letter-spacing:1px}
.hero-sub{font-family:"Montserrat",sans-serif;font-size:36px;font-weight:500;line-height:1.5;margin-top:6px}
.hero-dots{position:absolute;right:22px;top:225px;display:flex;flex-direction:column;gap:10px}
.hero-dots span{width:8px;height:8px;border-radius:50%;background:rgba(255,255,255,.55)}
.hero-dots span:first-child{background:var(--white)}
.hero-cut{position:absolute;left:0;bottom:0}

/* features */
.features{position:absolute;top:870px;left:0;width:1200px;display:flex;justify-content:center;gap:60px}
.feature{width:300px;text-align:center}
.feature-icon{width:70px;height:70px;margin:0 auto 18px;border-radius:50%;background:var(--cream);display:flex;align-items:center;justify-content:center}
.feature h3{font-size:22px;font-weight:600;line-height:1.25;color:var(--ink)}
.feature p{font-size:13px;color:var(--muted);line-height:1.5;margin-top:10px}
.feature .more{margin-top:8px}

/* split services */
.services{position:absolute;top:1180px;left:0;width:1200px;height:550px;display:flex;clip-path:polygon(0 0,50% 46px,100% 0,100% 100%,0 100%)}
.service{position:relative;width:600px;height:100%;color:var(--white);padding:215px 0 0 90px}
.service-quality{background:linear-gradient(135deg,#1e2f8c 0%,#15236a 60%,#0d1747 100%)}
.service-mdm{background:linear-gradient(135deg,#2a2c33 0%,#1c1d22 55%,#101114 100%)}
.service h2{font-size:30px;font-weight:600}
.service ul{margin-top:22px}
.service li{font-size:18px;display:flex;align-items:center;gap:12px;margin-bottom:14px}
.service li svg{flex:none}
.btn-light{display:inline-block;margin-top:22px;background:var(--white);color:var(--ink);font-size:12px;font-weight:600;padding:9px 20px;border-radius:16px}

/* connectors */
.connectors{position:absolute;top:1840px;left:0;width:1200px}
.section-title{text-align:center;font-size:40px;font-weight:600;color:var(--ink)}
.connector-grid{display:grid;grid-template-columns:310px 310px 310px;gap:40px 30px;justify-content:center;margin-top:58px}
.card{background:var(--white);border:1px solid var(--line);box-shadow:0 3px 8px rgba(0,0,0,.12);padding:22px 24px;display:flex;gap:16px;min-height:130px}
.card.tall{min-height:210px}
.card.highlight{background:var(--cream)}
.card h4{font-size:20px;font-weight:600;color:var(--ink)}
.card p{font-size:14px;color:var(--muted);line-height:1.45;margin-top:4px}
.card svg{flex:none;margin-top:2px}

/* partner strip */
.partners{position:absolute;top:2480px;left:0;width:1200px;height:100px;background:var(--grey-band);display:flex;align-items:center;justify-content:space-around;padding:0 60px}
.partner{display:flex;align-items:center;gap:10px;font-size:22px;font-weight:600;color:#8b8d92}
.partner i{width:16px;height:16px;border-radius:50%;background:#9d9fa4}

/* footer */
.site-footer{position:absolute;top:2600px;left:0;width:1200px;height:390px;background:var(--footer);color:var(--footer-text);display:grid;grid-template-columns:290px 220px 230px 270px;padding:60px 0 0 100px}
.site-footer h5{font-size:17px;font-weight:600;color:var(--white);letter-spacing:.5px;margin-bottom:28px}
.contact-list li{display:flex;gap:12px;font-size:13px;line-height:1.5;margin-bottom:18px}
.link-list li{font-size:13px;margin-bottom:10px;color:var(--footer-text)}
.link-list li::before{content:"•";margin-right:10px}
.social-list li{display:flex;align-items:center;gap:10px;font-size:13px;margin-bottom:16px}
.social-list i{width:16px;height:16px;border-radius:50%;background:var(--footer-text)}
.contact-form{display:flex;flex-direction:column;gap:10px}
.contact-form .field{width:270px;height:32px;background:var(--white);color:#888;font-size:12px;padding:8px 10px}
.contact-form .send{width:90px;height:30px;background:var(--send);color:var(--white);font-size:13px;display:flex;align-items:center;justify-content:center}
.footer-bar{position:absolute;top:2990px;left:0;width:1200px;height:50px;background:var(--footer-bar);color:#c6c7cb;font-size:13px;display:flex;align-items:center;justify-content:center}
</style>
</head>
<body>

<header class="site-header">
  <div class="brand-name">Zorbil Data</div>
  <nav class="main-nav">
    <span class="active">Home</span><span>About us</span><span>Our Services</span><span>Rich Connectors</span><span>Contact</span>
  </nav>
</header>

<section class="hero">
  <div class="hero-photo" role="img" aria-label="Photo of a person walking down a lit data center aisle between server racks"></div>
  <div class="hero-text">
    <h1 class="hero-title">Zorbil Data</h1>
    <p class="hero-sub">Enterprise Data Quality and Master<br>Data Management Made Easy</p>
  </div>
  <div class="hero-dots"><span></span><span></span><span></span></div>
  <svg class="hero-cut" width="1200" height="200" viewBox="0 0 1200 200" aria-hidden="true">
    <polygon points="0,60 600,170 1200,60 1200,200 0,200" fill="#ffffff"/>
    <polyline points="0,52 600,162 1200,52" fill="none" stroke="#f2b90f" stroke-width="12"/>
    <polygon points="0,70 600,180 1200,70 1200,200 0,200" fill="#ffffff"/>
  </svg>
</section>

<section class="features">
  <div class="feature">
    <div class="feature-icon">
      <svg width="40" height="32" viewBox="0 0 40 32" fill="none" stroke="#2b2f3a" stroke-width="2"><path d="M10 24h22a7 7 0 0 0 0-14 10 10 0 0 0-19-2A8 8 0 0 0 10 24z"/><path d="M20 30V16m-5 5 5-5 5 5"/></svg>
    </div>
    <h3>Cleanse addresses<br>in 5 minutes</h3>
    <p>Adapt to changing data with fast, reliable pipelines that keep every record clean and ready for insight.</p>
    <svg class="more" width="14" height="10" viewBox="0 0 14 10" fill="none" stroke="#2b2f3a" stroke-width="2"><path d="M2 2l5 5 5-5"/></svg>
  </div>
  <div class="feature">
    <div class="feature-icon">
      <svg width="34" height="38" viewBox="0 0 34 38" fill="none" stroke="#2b2f3a" stroke-width="2"><rect x="3" y="3" width="28" height="32" rx="2"/><path d="M9 12h16M9 18h16M9 24h10"/></svg>
    </div>
    <h3>Match and Merge<br>records in 10 minutes</h3>
    <p>Find duplicate entries across your systems and combine them into one trusted view within minutes today.</p>
    <svg class="more" width="14" height="10" viewBox="0 0 14 10" fill="none" stroke="#2b2f3a" stroke-width="2"><path d="M2 2l5 5 5-5"/></svg>
  </div>
  <div class="feature">
    <div class="feature-icon">
      <svg width="38" height="36" viewBox="0 0 38 36" fill="none" stroke="#2b2f3a" stroke-width="2"><path d="M19 3 35 11 19 19 3 11z"/><path d="M3 18l16 8 16-8M3 25l16 8 16-8"/></svg>
    </div>
    <h3>Master records<br>in 60 minutes</h3>
    <p>Build golden records that every team can rely on, with clear rules and full control over data.</p>
    <svg class="more" width="14" height="10" viewBox="0 0 14 10" fill="none" stroke="#2b2f3a" stroke-width="2"><path d="M2 2l5 5 5-5"/></svg>
  </div>
</section>

<section class="services">
  <div class="service service-quality" role="img" aria-label="Deep blue photo backdrop of abstract data network">
    <h2>Data Quality</h2>
    <ul>
      <li><svg width="18" height="18" viewBox="0 0 18 18"><circle cx="9" cy="9" r="8" fill="#fff"/><path d="M5 9l3 3 5-6" stroke="#1b2f8a" stroke-width="2" fill="none"/></svg>Global Address Verification</li>
      <li><svg width="18" height="18" viewBox="0 0 18 18"><circle cx="9" cy="9" r="8" fill="#fff"/><path d="M5 9l3 3 5-6" stroke="#1b2f8a" stroke-width="2" fill="none"/></svg>Data Cleansing/Enrichment</li>
      <li><svg width="18" height="18" viewBox="0 0 18 18"><circle cx="9" cy="9" r="8" fill="#fff"/><path d="M5 9l3 3 5-6" stroke="#1b2f8a" stroke-width="2" fill="none"/></svg>Match and Merge</li>
    </ul>
    <span class="btn-light">Learn More</span>
  </div>
  <div class="service service-mdm" role="img" aria-label="Dark photo backdrop of a connected city at night">
    <h2>Master Data Management</h2>
    <ul>
      <li><svg width="18" height="18" viewBox="0 0 18 18"><circle cx="9" cy="9" r="8" fill="#fff"/><path d="M5 9l3 3 5-6" stroke="#1c1d22" stroke-width="2" fill="none"/></svg>Integration</li>
      <li><svg width="18" height="18" viewBox="0 0 18 18"><circle cx="9" cy="9" r="8" fill="#fff"/><path d="M5 9l3 3 5-6" stroke="#1c1d22" stroke-width="2" fill="none"/></svg>Mastering</li>
      <li><svg width="18" height="18" viewBox="0 0 18 18"><circle cx="9" cy="9" r="8" fill="#fff"/><path d="M5 9l3 3 5-6" stroke="#1c1d22" stroke-width="2" fill="none"/></svg>Governance</li>
    </ul>
    <span class="btn-light">Learn More</span>
  </div>
</section>

<section class="connectors">
  <h2 class="section-title">Rich Connectors</h2>
  <div class="connector-grid">
    <div class="card tall">
      <svg width="30" height="32" viewBox="0 0 30 32" fill="none" stroke="#2b3aa8" stroke-width="2"><rect x="3" y="3" width="20" height="26" rx="2"/><path d="M8 11h10M8 16h10M8 21h6M22 22l5 5"/></svg>
      <div><h4>Applications</h4><p>Tarnwick CRM<br>Fieldrova<br>Kestrel<br>Norvane Business Suite</p></div>
    </div>
    <div class="card tall highlight">
      <svg width="30" height="32" viewBox="0 0 30 32" fill="none" stroke="#2b3aa8" stroke-width="2"><ellipse cx="15" cy="7" rx="11" ry="4"/><path d="M4 7v18c0 2 5 4 11 4s11-2 11-4V7M4 16c0 2 5 4 11 4s11-2 11-4"/></svg>
      <div><h4>Databases</h4><p>Norvane DB<br>Quillbase<br>Halden SQL Server<br>Pelliqo SQL<br>Varstone DB</p></div>
    </div>
    <div class="card tall">
      <svg width="30" height="32" viewBox="0 0 30 32" fill="none" stroke="#2b3aa8" stroke-width="2"><path d="M5 3h14l7 7v19H5z"/><path d="M19 3v7h7"/></svg>
      <div><h4>Files</h4><p>CSV<br>Delimited<br>Sheetwise</p></div>
    </div>
    <div class="card">
      <svg width="30" height="32" viewBox="0 0 30 32" fill="none" stroke="#2b3aa8" stroke-width="2"><rect x="3" y="6" width="24" height="22" rx="2"/><path d="M3 12h24M9 3v6M21 3v6"/></svg>
      <div><h4>Batch</h4><p>On your schedule</p></div>
    </div>
    <div class="card">
      <svg width="30" height="32" viewBox="0 0 30 32" fill="none" stroke="#2b3aa8" stroke-width="2"><path d="M3 10c6-5 18-5 24 0M6 16c5-4 13-4 18 0M10 22c3-2 7-2 10 0"/><circle cx="15" cy="27" r="2"/></svg>
      <div><h4>Streaming</h4><p>Always in sync</p></div>
    </div>
    <div class="card">
      <svg width="30" height="32" viewBox="0 0 30 32" fill="none" stroke="#2b3aa8" stroke-width="2"><circle cx="15" cy="16" r="12"/><path d="M15 9v7l5 3"/></svg>
      <div><h4>Real Time/Interactive</h4><p>Autocomplete Anything<br>Smart Search</p></div>
    </div>
  </div>
</section>

<section class="partners">
  <span class="partner"><i></i>tunegrove</span>
  <span class="partner"><i></i>scriptvale</span>
  <span class="partner"><i></i>marketly</span>
  <span class="partner"><i></i>pixelbrook</span>
  <span class="partner"><i></i>snapmeadow</span>
</section>

<footer class="site-footer">
  <div>
    <h5>CONTACT US</h5>
    <ul class="contact-list">
      <li><svg width="14" height="18" viewBox="0 0 14 18"><path d="M7 1a6 6 0 0 0-6 6c0 4.5 6 10 6 10s6-5.5 6-10a6 6 0 0 0-6-6z" fill="#cfd0d4"/><circle cx="7" cy="7" r="2" fill="#17181c"/></svg><span>42 Orchard Row, Dunhaven,<br>WA 98021</span></li>
      <li><svg width="14" height="16" viewBox="0 0 14 16"><path d="M3 1l3 3-2 2c1 2 3 4 5 5l2-2 3 3-2 3C6 15 0 9 1 3z" fill="#cfd0d4"/></svg><span>(555) 010-2748</span></li>
      <li><svg width="14" height="14" viewBox="0 0 14 14"><rect x="1" y="3" width="12" height="9" fill="#cfd0d4"/><path d="M1 3l6 5 6-5" stroke="#17181c" fill="none"/></svg><span>info@zorbilinfo.example</span></li>
    </ul>
  </div>
  <div>
    <h5>QUICK LINKS</h5>
    <ul class="link-list">
      <li>Home</li><li>About us</li><li>Rich Connectors</li><li>Services</li><li>Contact Us</li>
    </ul>
  </div>
  <div>
    <h5>FOLLOW US</h5>
    <ul class="social-list">
      <li><i></i>Friendnet</li><li><i></i>Chirpline</li><li><i></i>Circlepage</li><li><i></i>Vidstream</li>
    </ul>
  </div>
  <div>
    <h5>GET IN TOUCH</h5>
    <div class="contact-form">
      <div class="field">Your Name</div>
      <div class="field">Email address</div>
      <div class="field">Phone</div>
      <div class="send">SEND</div>
    </div>
  </div>
</footer>
<div class="footer-bar">© Copyright 2018 . All Rights Reserved. Terms and Conditions | Privacy Policy</div>

</body>
</html>
```